New stationary design for online film company

We need some new stationary to fit with our new logo. The stationary should be professional, clean and simple.
We need designs for a full set of business stationary.
We need - letterhead, envelopes, invoices, proposals, coverslip/note and cover page

Industry/Entity Type

Business

```html
<!DOCTYPE html>
<html lang="en">
<head>
<meta charset="utf-8">
<title>Reelwave Folder Covers</title>
<link rel="stylesheet" href="https://fonts.googleapis.com/css2?family=Mulish:wght@400;600;700&display=swap">
<style>
  :root {
    --stage: #e9e7e3;
    --cover-blue: #0a3d66;
    --cover-blue-light: #0f4d80;
    --cover-blue-deep: #083456;
    --motif: rgba(255, 255, 255, 0.05);
    --text-light: #dfe6ee;
    --tagline: #7fa3c4;
  }
  * { box-sizing: border-box; margin: 0; padding: 0; }
  html, body {
    width: 1200px;
    height: 720px;
    overflow: hidden;
    background: var(--stage);
    font-family: "Mulish", Arial, sans-serif;
  }
  .spread {
    width: 1200px;
    height: 720px;
    display: flex;
    justify-content: center;
    align-items: center;
    gap: 48px;
  }
  .cover {
    position: relative;
    width: 440px;
    height: 600px;
    overflow: hidden;
    background: linear-gradient(160deg, var(--cover-blue-light) 0%, var(--cover-blue) 55%, var(--cover-blue-deep) 100%);
    box-shadow: 0 10px 30px rgba(0, 0, 0, 0.18);
  }
  .motif-circle {
    position: absolute;
    border-radius: 50%;
    background: var(--motif);
  }
  .cover--back .motif-circle {
    width: 420px; height: 420px;
    right: -260px; top: 170px;
  }
  .cover--front .motif-circle {
    width: 460px; height: 460px;
    left: -30px; top: 40px;
  }
  .contact {
    position: absolute;
    left: 0; right: 0;
    top: 410px;
    text-align: center;
    color: var(--text-light);
    font-size: 9.5px;
    line-height: 1.45;
    letter-spacing: 0.02em;
  }
  .contact .address { margin-top: 6px; }
  .contact .web { margin-top: 6px; }
  .brand {
    position: absolute;
    left: 0; right: 0;
    top: 400px;
    display: flex;
    flex-direction: column;
    align-items: center;
  }
  .brand-name {
    display: flex;
    align-items: center;
    gap: 10px;
    color: var(--text-light);
    font-size: 34px;
    font-weight: 700;
    letter-spacing: 0.01em;
  }
  .brand-dot {
    width: 26px; height: 26px;
    border-radius: 50%;
    background: var(--text-light);
  }
  .tagline {
    margin-top: 14px;
    color: var(--tagline);
    font-size: 10px;
    font-weight: 600;
    letter-spacing: 0.12em;
    text-transform: uppercase;
  }
</style>
</head>
<body>
  <main class="spread">
    <section class="cover cover--back" aria-label="Back cover">
      <div class="motif-circle"></div>
      <address class="contact" style="font-style: normal;">
        <div>t&nbsp; 555-014-2280</div>
        <div>m 555-017-3364</div>
        <div>e&nbsp; hello@reelwave.com</div>
        <div class="address">18 Harbor Lane Suite 4<br>Portland ME 04101 USA</div>
        <div class="web">www.reelwave.com</div>
      </address>
    </section>
    <section class="cover cover--front" aria-label="Front cover">
      <div class="motif-circle"></div>
      <div class="brand">
        <div class="brand-name"><span class="brand-dot"></span>reelwave</div>
        <div class="tagline">Online Film Production &amp; Strategy</div>
      </div>
    </section>
  </main>
</body>
</html>
```